Business Card design for insurance broker in Denver, CO, USA

I need a business card designed using this logo that was just created. We sell life and disability income insurance to US consumers.
Looking for a professionally designed card to make use of the logo and have something to hand to prospects or new business referral sources. The card could be white, gray, black or whatever you would recommend.

Target Market(s)

US Consumers and other financial professionals that I partner with.

Industry/Entity Type

Insurance Broker

Contact Information for Business Card

Owen R. Tessler, CFP, RHU (please note that CLU should have a superscript R in a circle for registered trademark)
President
phone (303) 555-0147
email owen@brightlakecoverage.com
4620 W. Hollister Rd, Suite 310, Greenwood Village, CO 80111
Somewhere fit in a tagline saying "Your guide to life, long term care, and income protection plans" (maybe the back if it doesn't fit on the front, your call)

Font styles to use
Sans Serif

Requirements
Must have
• Must have logo in correct blue and gray colors, my name, address, phone, email. Order and placement determined by the designer.
• I just want something that looks a more professional than what I could have done using the business card designer tool on printmakerhub.com or CardNest, or any other do-it-yourself tool
• A regular rectangular business card with square corners is preferred
Nice to have
• I included the logos of 2 organizations I belong to (GQLF and BEPWO). They should be small, but visible on the back only. If it doesn’t look good, this is not a requirement, feel free to drop it.
Should not have
• Do not add any colors not already in the logo, except use of black and whites which are okay. If you use the logo on the back and want to make that in all black, gray or white, that may be okay as well.

```html
<!DOCTYPE html>
<html lang="en">
<head>
<meta charset="UTF-8">
<title>Brightlake Coverage – Business Card</title>
<link href="https://fonts.googleapis.com/css2?family=Poppins:wght@400;500;600&display=swap" rel="stylesheet">
<style>
  :root {
    --stage: #cbcbcb;
    --brand-blue: #2391d3;
    --brand-blue-text: #2a8fd0;
    --ink: #111315;
    --card-white: #ffffff;
    --card-grey: #e4e5e7;
    --band-grey: #e9e9eb;
    --white: #ffffff;
  }
  * { margin: 0; padding: 0; box-sizing: border-box; }
  html, body {
    width: 966px; height: 1200px; overflow: hidden;
    background: var(--stage);
    font-family: "Poppins", sans-serif;
  }
  .canvas { position: relative; width: 966px; height: 1200px; }

  .card {
    position: absolute; left: 127px; width: 712px; height: 407px;
    box-shadow: 2px 3px 6px rgba(0,0,0,0.28);
    overflow: hidden;
  }
  .card--front {
    top: 128px;
    background: linear-gradient(120deg, var(--card-white) 0%, var(--card-white) 20%, var(--card-grey) 100%);
  }
  .card--back { top: 663px; background: var(--brand-blue); }

  .brand { position: absolute; display: flex; align-items: center; }
  .brand__dot { flex: none; border-radius: 50%; border-style: solid; }
  .brand__name { font-weight: 500; text-transform: uppercase; line-height: 1.02; }

  .card--front .brand { left: 37px; top: 36px; gap: 10px; }
  .card--front .brand__dot { width: 54px; height: 54px; border-width: 3px; border-color: var(--brand-blue); }
  .card--front .brand__name { color: var(--brand-blue); font-size: 20px; }

  .card--back .brand { left: 50%; top: 130px; transform: translateX(-50%); gap: 18px; }
  .card--back .brand__dot { width: 112px; height: 112px; border-width: 5px; border-color: var(--white); }
  .card--back .brand__name { color: var(--white); font-size: 35px; }

  .holder { position: absolute; left: 64px; top: 132px; }
  .holder__name {
    font-weight: 600; font-size: 30px; letter-spacing: 1.6px; color: var(--ink);
    line-height: 1.2;
  }
  .holder__name sup { font-size: 11px; font-weight: 500; vertical-align: 18px; letter-spacing: 0; }
  .holder__title {
    margin-top: 5px; font-size: 20px; letter-spacing: 3px; color: var(--ink); font-weight: 400;
  }
  .contact { list-style: none; margin-top: 7px; }
  .contact li {
    font-size: 18px; letter-spacing: 0.6px; color: var(--brand-blue-text);
    line-height: 36.5px;
  }

  .tagline-band {
    position: absolute; left: 0; right: 0; bottom: 0; height: 34px;
    display: flex; align-items: center; justify-content: center;
    font-size: 18px; letter-spacing: 0.3px;
  }
  .card--front .tagline-band { background: var(--brand-blue); color: var(--white); }
  .card--back .tagline-band { background: var(--band-grey); color: var(--brand-blue-text); }
</style>
</head>
<body>
<main class="canvas">

  <section class="card card--front" aria-label="Card front">
    <div class="brand">
      <span class="brand__dot"></span>
      <span class="brand__name">Brightlake<br>Coverage</span>
    </div>

    <div class="holder">
      <h1 class="holder__name">Owen R. Tessler, CFP<sup>™</sup>, RHU</h1>
      <p class="holder__title">PRESIDENT</p>
      <ul class="contact">
        <li>(303) 555-0147</li>
        <li>owen@brightlakecoverage.com</li>
        <li>4620 W. Hollister Rd, Suite 310</li>
        <li>Cedar Hollow, CO 80299</li>
      </ul>
    </div>

    <p class="tagline-band">Your guide to life, long term care, and income protection plans</p>
  </section>

  <section class="card card--back" aria-label="Card back">
    <div class="brand">
      <span class="brand__dot"></span>
      <span class="brand__name">Brightlake<br>Coverage</span>
    </div>
    <p class="tagline-band">Your guide to life, long term care, and income protection plans</p>
  </section>

</main>
</body>
</html>
```